Quorvane Capital Modern Business Card

We need a modern business card template designed for Quorvane Capital.
Quorvane Capital is a diversified global cryptocurrency investment fund.

The font under the logo: Hiragino Kaku Gothic Pro

Color Hexcode: Main colors white (ffffff) & teal (188383), we are open to adding #fcca46 as an accent

Target Market(s)

Accredited Investors, high net worth individuals and institutional investors

Industry/Entity Type

Investment

Contact Information for Business Card

Contact Information should contain
Name
main phone +1 720 555 0147
cell
email

Font styles to use
Sans Serif
Other font styles liked:
• Hiragino Kaku Gothic Pro

Requirements
Must have
• would like to have icons that identify the contact information
• include our website: www.quorvanecapital.example
• include our Tagline: Diversified Crypto Investment Funds
Nice to have
• Would like to have a simple back side with the logo (without the words) and plenty of space

```html
<!DOCTYPE html>
<html lang="en">
<head>
<meta charset="utf-8">
<title>Quorvane Capital Business Card</title>
<link rel="stylesheet" href="https://fonts.googleapis.com/css2?family=Roboto:wght@400;500&family=Roboto+Condensed:wght@700&display=swap">
<style>
  :root {
    --backdrop: #1e1e1e;
    --paper: #f3f3f3;
    --teal: #1a9390;
    --ink: #111111;
    --grey: #4a4a4a;
    --pattern: #e6eeee;
  }
  * { margin: 0; padding: 0; box-sizing: border-box; }
  html, body { width: 1200px; height: 960px; overflow: hidden; }
  body {
    background: var(--backdrop);
    position: relative;
    font-family: "Roboto", Arial, sans-serif;
  }
  .card {
    position: absolute;
    width: 600px;
    height: 342px;
    background: var(--paper);
    box-shadow: 0 4px 10px rgba(0,0,0,0.5);
  }
  .card--front { left: 314px; top: 113px; }
  .card--back { left: 311px; top: 472px; }

  .brand {
    position: absolute;
    left: 32px;
    top: 148px;
    display: flex;
    align-items: center;
    gap: 8px;
  }
  .brand__square { width: 12px; height: 12px; background: var(--teal); }
  .brand__name {
    font-size: 19px;
    font-weight: 400;
    letter-spacing: 0.2px;
    color: var(--ink);
  }

  .person { position: absolute; left: 32px; top: 240px; }
  .person__name {
    font-family: "Roboto Condensed", Arial, sans-serif;
    font-weight: 700;
    font-size: 22px;
    color: var(--teal);
    line-height: 26px;
  }
  .person__role {
    font-family: "Roboto Condensed", Arial, sans-serif;
    font-weight: 700;
    font-size: 15px;
    color: var(--ink);
    line-height: 18px;
  }

  .contact { position: absolute; left: 316px; top: 213px; list-style: none; }
  .contact__item {
    display: flex;
    align-items: center;
    gap: 8px;
    font-size: 14.5px;
    color: var(--grey);
    line-height: 19px;
  }
  .contact__icon { width: 14px; height: 14px; fill: var(--teal); flex: none; }
  .tagline {
    position: absolute;
    left: 316px;
    top: 291px;
    font-size: 14px;
    font-weight: 500;
    color: var(--grey);
  }

  .band { position: absolute; left: 0; bottom: 0; height: 12px; display: flex; width: 600px; }
  .band__teal { width: 297px; background: var(--teal); }
  .band__gap { width: 3px; background: #ffffff; }
  .band__dark { flex: 1; background: var(--ink); }

  .back-pattern {
    position: absolute;
    inset: 0;
    background: linear-gradient(180deg, var(--pattern), #eef2f2);
  }
  .back-brand {
    position: absolute;
    right: 50px;
    bottom: 48px;
    font-size: 16px;
    font-weight: 400;
    color: var(--teal);
  }
</style>
</head>
<body>
  <section class="card card--front">
    <div class="brand">
      <span class="brand__square"></span>
      <span class="brand__name">QUORVANE CAPITAL</span>
    </div>

    <div class="person">
      <p class="person__name">DANIEL MERCER</p>
      <p class="person__role">CO-FOUNDER</p>
    </div>

    <ul class="contact">
      <li class="contact__item">
        <svg class="contact__icon" viewBox="0 0 16 16"><path d="M3.6 1.2l2.3 2.4-1.3 2a9 9 0 0 0 5.8 5.8l2-1.3 2.4 2.3-1.6 2.1C7 14.6 1.4 9 1.5 2.8z"/></svg>
        <span>+1 720 555 0147</span>
      </li>
      <li class="contact__item">
        <svg class="contact__icon" viewBox="0 0 16 16"><path d="M4 0h8a1 1 0 0 1 1 1v14a1 1 0 0 1-1 1H4a1 1 0 0 1-1-1V1a1 1 0 0 1 1-1zm1 2v10h6V2zm3 11a1 1 0 1 0 0 2 1 1 0 0 0 0-2z" fill-rule="evenodd"/></svg>
        <span>+1 720 555 0162</span>
      </li>
      <li class="contact__item">
        <svg class="contact__icon" viewBox="0 0 16 16"><path d="M1 3h14v1.2L8 9 1 4.2zM1 6l7 4.7L15 6v7H1z"/></svg>
        <span>daniel@quorvanecapital.example</span>
      </li>
      <li class="contact__item">
        <svg class="contact__icon" viewBox="0 0 16 16"><path d="M8 1a7 7 0 1 0 0 14A7 7 0 0 0 8 1zm-1 2.2c-.6 1-1.8 1.4-2.6 2.4.8.6 1.9.2 2.6 1 .6.8-.2 1.8.5 2.6.6.6 1.4.9 1.2 2.2l-.4 1.4A5.6 5.6 0 0 1 2.4 8 5.6 5.6 0 0 1 7 3.2zm3 .5a5.6 5.6 0 0 1 3.4 6.4c-.7-.3-1.4-.9-1.6-1.8-.2-1 .4-2.1-.5-2.6-.6-.3-1.5.2-1.8-.6-.2-.6.3-1 .5-1.4z"/></svg>
        <span>www.quorvanecapital.example</span>
      </li>
    </ul>
    <p class="tagline">Diversified Crypto Investment Funds</p>

    <div class="band">
      <span class="band__teal"></span>
      <span class="band__gap"></span>
      <span class="band__dark"></span>
    </div>
  </section>

  <section class="card card--back">
    <div class="back-pattern" role="img" aria-label="Faint repeating geometric background pattern in pale teal"></div>
    <span class="back-brand">QUORVANE CAPITAL</span>
  </section>
</body>
</html>
```